Business card

creative business card for newly created national firm that specializes in high-density storage for retail markets. Looking for creativity and overall theme that will differentiate from others in this unique niche ...essentially a design that will provide instant recognition as we develop our identity in the marketplace. possible initial thoughts are attached with logo separately

Industry/Entity Type

Retail

```html
<!DOCTYPE html>
<html lang="en">
<head>
<meta charset="utf-8">
<title>Tallbay Storage – Business Card</title>
<link rel="stylesheet" href="https://fonts.googleapis.com/css2?family=Federo&family=Open+Sans:wght@400;700&display=swap">
<style>
  :root {
    --navy: #184a6b;
    --deep-blue: #1d5f86;
    --mid-blue: #3a9cc0;
    --aqua: #5fe3f2;
    --ink: #111111;
    --paper: #ffffff;
  }
  html, body {
    margin: 0;
    padding: 0;
    width: 1200px;
    height: 686px;
    overflow: hidden;
    background: var(--paper);
  }
  .card {
    position: relative;
    width: 1200px;
    height: 686px;
    background: var(--paper);
    overflow: hidden;
    font-family: "Open Sans", Arial, sans-serif;
  }
  .side-wave {
    position: absolute;
    left: 0;
    top: 0;
    width: 340px;
    height: 686px;
  }
  .brand {
    position: absolute;
    left: 438px;
    top: 56px;
    display: flex;
    align-items: center;
    gap: 22px;
  }
  .brand-square {
    width: 92px;
    height: 92px;
    background: var(--mid-blue);
  }
  .brand-name {
    font-family: "Federo", sans-serif;
    font-weight: 400;
    color: var(--deep-blue);
    font-size: 68px;
    line-height: 0.98;
    letter-spacing: 1px;
  }
  .content {
    position: absolute;
    left: 300px;
    right: 0;
    text-align: center;
  }
  .person-name {
    top: 278px;
    margin: 0;
    font-weight: 700;
    font-size: 72px;
    line-height: 1.2;
    color: var(--navy);
    letter-spacing: 1px;
    text-shadow: 1px 2px 3px rgba(0,0,0,0.25);
  }
  .phone {
    top: 372px;
    font-size: 32px;
    color: var(--ink);
    letter-spacing: 0.5px;
  }
  .tagline {
    top: 496px;
    font-family: "Federo", sans-serif;
    font-size: 58px;
    letter-spacing: 3px;
    color: var(--deep-blue);
  }
  .website {
    top: 570px;
    font-size: 30px;
    color: var(--ink);
  }
</style>
</head>
<body>
  <main class="card">
    <svg class="side-wave" viewBox="0 0 340 686" role="img" aria-label="Blue gradient side band with faint repeated brand pattern">
      <defs>
        <linearGradient id="wave-fill" x1="0" y1="0" x2="1" y2="0">
          <stop offset="0" stop-color="#1d6f93"/>
          <stop offset="0.55" stop-color="#33b4d4"/>
          <stop offset="1" stop-color="#63eefa"/>
        </linearGradient>
      </defs>
      <path d="M0 0 H262 C300 70 318 170 306 250 C294 330 222 400 222 480 C222 560 282 620 286 686 H0 Z" fill="url(#wave-fill)"/>
      <path d="M262 0 C300 70 318 170 306 250 C294 330 222 400 222 480 C222 560 282 620 286 686" fill="none" stroke="var(--navy)" stroke-width="4"/>
    </svg>

    <div class="brand">
      <div class="brand-square"></div>
      <div class="brand-name">TALLBAY<br>STORAGE</div>
    </div>

    <h1 class="content person-name">Daniel Marsh</h1>
    <div class="content phone">855-SHELF-PLUS</div>
    <div class="content tagline">MAXIMIZE EVERY AISLE</div>
    <div class="content website">www.tallbaystorage.com</div>
  </main>
</body>
</html>
```